Business Strategy Company
Cards & Paper for Enterprise Collaboration Data Company
Project: Business Strategy Company
Business Strategy Company -
Creative Brief
Professional
Tobin G. Maraselt
CEO
31927 Harrowgate Ave. Suite 400 Berkley, CA 90388
tobin@quandelrox.example
www.quandelrox.example
Please include tagline: "Collaboration Intelligence" We would like a clean, modern card like the types found in these designs: https://www.pendlewick.example/drafts/display/contest/93587/draft/705568 https://www.pendlewick.example/drafts/display/contest/79787/draft/600578 https://www.pendlewick.example/drafts/display/contest/77433/draft/650842 https://www.pendlewick.example/drafts/display/contest/50102/draft/406651 https://www.pendlewick.example/drafts/display/contest/101628/draft/769948 https://www.pendlewick.example/drafts/display/contest/101641/draft/771307 https://www.pendlewick.example/drafts/display/contest/99022/draft/771303
We like a field of dark color or a gradient with the logo in either white or a color just slightly lighter/darker than the background (i.e. if the background is black, the logo would either be white or very dark gray). We'd like to see both.

```html
<!DOCTYPE html>
<html lang="en">
<head>
<meta charset="utf-8">
<title>quandelrox — Stationery</title>
<link rel="stylesheet" href="https://fonts.googleapis.com/css2?family=Questrial&display=swap">
<style>
  :root {
    --bg: #ecebe8;
    --paper: #ffffff;
    --navy: #1f2a5c;
    --cyan: #25aed3;
    --cyan-deep: #0d86ad;
    --cyan-light: #5fd0ec;
    --gray: #6d6e71;
    --shadow: 0 6px 18px rgba(0,0,0,.18);
  }
  * { box-sizing: border-box; margin: 0; padding: 0; }
  html, body { width: 1200px; height: 899px; overflow: hidden; }
  body {
    background: var(--bg);
    font-family: "Questrial", sans-serif;
    color: var(--navy);
    position: relative;
  }
  .sheet { position: absolute; background: var(--paper); box-shadow: var(--shadow); }

  .brand { display: flex; align-items: center; gap: 8px; color: var(--navy); }
  .brand-mark { width: 14px; height: 14px; background: var(--cyan); border-radius: 3px; }
  .brand-name { font-size: 22px; letter-spacing: .5px; }
  .brand--light { color: #fff; }
  .brand--light .brand-mark { background: #fff; }

  .contact { font-size: 9px; line-height: 1.6; color: var(--gray); }

  /* Letterhead */
  .letterhead { left: 50px; top: 60px; width: 430px; height: 608px; padding: 40px 36px; }
  .letterhead .contact { position: absolute; right: 36px; top: 44px; text-align: right; }

  /* Business cards */
  .card { width: 300px; height: 171px; border-radius: 12px; padding: 22px 24px; }
  .card--front {
    left: 530px; top: 60px;
    background: linear-gradient(135deg, var(--cyan-light), var(--cyan) 50%, var(--cyan-deep));
    display: flex; flex-direction: column; align-items: center; justify-content: center; gap: 10px;
  }
  .tagline { font-size: 11px; letter-spacing: 1px; }
  .card--front .tagline { color: #fff; }
  .card--tagline { left: 860px; top: 60px; display: flex; align-items: center; justify-content: center; }
  .card--tagline .tagline { color: var(--gray); }
  .card--contact { left: 530px; top: 262px; display: flex; flex-direction: column; justify-content: space-between; }
  .person-name { font-size: 13px; color: var(--navy); }
  .person-role { font-size: 9px; color: var(--cyan); margin-bottom: 4px; }
  .card--contact .brand-name { font-size: 18px; }

  /* Envelopes */
  .envelope { width: 330px; height: 165px; top: 500px; }
  .envelope--front { left: 530px; padding: 20px 22px; }
  .envelope--front .brand-name { font-size: 16px; }
  .envelope--front .contact { margin-top: 8px; }
  .envelope--back { left: 870px; overflow: hidden; }
  .envelope--back svg { display: block; }
</style>
</head>
<body>

  <section class="sheet letterhead" aria-label="Letterhead">
    <div class="brand"><span class="brand-mark"></span><span class="brand-name">quandelrox</span></div>
    <address class="contact">
      31927 Harrowgate Ave. Suite 400<br>
      Berkley, CA 90388<br>
      tobin@quandelrox.example<br>
      www.quandelrox.example
    </address>
  </section>

  <section class="sheet card card--front" aria-label="Business card front">
    <div class="brand brand--light"><span class="brand-mark"></span><span class="brand-name">quandelrox</span></div>
    <p class="tagline">Collaboration Intelligence</p>
  </section>

  <section class="sheet card card--tagline" aria-label="Business card back">
    <p class="tagline">Collaboration Intelligence</p>
  </section>

  <section class="sheet card card--contact" aria-label="Business card contact side">
    <div class="brand"><span class="brand-mark"></span><span class="brand-name">quandelrox</span></div>
    <div>
      <p class="person-name">Tobin G. Maraselt</p>
      <p class="person-role">CEO</p>
      <address class="contact">
        31927 Harrowgate Ave. Suite 400 Berkley, CA 90388<br>
        tobin@quandelrox.example · www.quandelrox.example
      </address>
    </div>
  </section>

  <section class="sheet envelope envelope--front" aria-label="Envelope front">
    <div class="brand"><span class="brand-mark"></span><span class="brand-name">quandelrox</span></div>
    <address class="contact">
      31927 Harrowgate Ave. Suite 400<br>
      Berkley, CA 90388
    </address>
  </section>

  <section class="sheet envelope envelope--back" aria-label="Envelope back">
    <svg width="330" height="165" viewBox="0 0 330 165">
      <defs>
        <linearGradient id="flap" x1="0" y1="0" x2="0" y2="1">
          <stop offset="0" stop-color="#5fd0ec"/>
          <stop offset="1" stop-color="#0d86ad"/>
        </linearGradient>
      </defs>
      <path d="M0 0 H330 L195 82 Q165 98 135 82 Z" fill="url(#flap)"/>
      <path d="M0 165 L140 90 M330 165 L190 90" stroke="#e3e3e3" stroke-width="1" fill="none"/>
    </svg>
  </section>

</body>
</html>
```